IT Company based on Biology Business Needs a PowerPoint Design

We need a powerpoint design for a new company called 'Vast KELP'. We develop the machine learning solutions especially focused on deep learning algorithms for biology industry. Our initial product is a vision detection on biological images to help doctors diagnose the symptoms. We would like to see designs that use the color green.

Industry/Entity Type

Biotechnology

Requirements
Nice to have
• Lots of slide templates with company logo's look and feel

```html
<!DOCTYPE html>
<html lang="en">
<head>
<meta charset="utf-8">
<title>Vast KELP – Slide Templates</title>
<link rel="stylesheet" href="https://fonts.googleapis.com/css2?family=Titillium+Web:wght@300;400;600&display=swap">
<style>
  :root{
    --green:#7ac143;
    --green-dark:#138a3e;
    --backdrop:#cccccc;
    --paper:#ffffff;
    --ink:#222222;
    --ink-warm:#4a3a1c;
    --muted:#666666;
  }
  *{box-sizing:border-box;margin:0;padding:0}
  html,body{width:1200px;height:1200px;overflow:hidden;background:var(--backdrop)}
  body{position:relative;font-family:"Titillium Web",sans-serif;color:var(--ink)}

  .slide{position:absolute;width:512px;height:384px;background:var(--paper);overflow:hidden;
    box-shadow:6px 8px 10px rgba(0,0,0,.28)}
  .slide--cover{left:64px;top:191px}
  .slide--contents{left:634px;top:191px}
  .slide--article{left:64px;top:628px}
  .slide--closing{left:634px;top:628px}

  /* brand name */
  .brand{position:absolute;display:flex;align-items:center;gap:8px;color:var(--green);font-weight:400;white-space:nowrap;letter-spacing:-.5px}
  .brand__dot{width:.45em;height:.45em;border-radius:50%;background:var(--green)}
  .brand--large{font-size:34px}
  .brand--small{font-size:13px;gap:4px}

  /* cover */
  .cover__brand{left:170px;top:118px}
  .cover__band{position:absolute;left:0;top:214px;width:100%;height:54px;background:var(--green);
    display:flex;align-items:center;justify-content:center;color:#fff;font-weight:300;font-size:33px;letter-spacing:1px}
  .cover__subtitle{position:absolute;left:0;top:282px;width:100%;text-align:center;font-weight:300;font-size:16.5px;line-height:17px;letter-spacing:.4px}

  /* header for inner slides */
  .header__mark{position:absolute;left:0;top:23px}
  .header__title{position:absolute;left:59px;top:16px;font-weight:300;font-size:20px;letter-spacing:.6px;color:var(--ink)}
  .header__brand{position:absolute;left:406px;top:22px}

  /* footer */
  .footer{position:absolute;left:0;top:369px;width:100%;height:15px}
  .footer__url{position:absolute;right:0;top:0;height:15px;width:146px;display:flex;align-items:center;padding-left:26px;
    color:#fff;font-size:6px;letter-spacing:.2px}

  /* contents */
  .toc{position:absolute;left:61px;top:62px;width:412px;list-style:none}
  .toc__row{display:flex;align-items:flex-end;height:16.6px;font-size:8.5px;color:var(--ink-warm)}
  .toc__row--sub{padding-left:25px;font-size:6.5px;color:var(--muted)}
  .toc__label{white-space:nowrap}
  .toc__leader{flex:1;border-bottom:1px dotted #888;margin:0 0 3px 3px}
  .toc__page{width:40px;text-align:right;font-size:7.5px;color:var(--ink-warm);padding-right:8px}

  /* article */
  .article__heading{position:absolute;left:59px;top:54px;font-size:16px;font-weight:400;color:var(--ink-warm);letter-spacing:.2px}
  .article__columns{position:absolute;left:57px;top:81px;width:440px;height:268px;columns:2;column-gap:12px;overflow:hidden}
  .article__columns p{font-size:6.9px;line-height:11.4px;text-align:justify;margin-bottom:11.4px;color:#333}

  /* closing */
  .closing__brand{left:176px;top:212px}
  .closing__band{position:absolute;left:0;top:301px;width:100%;height:14px;background:var(--green);
    display:flex;align-items:center;justify-content:center;gap:16px;color:#fff;font-size:6px}
  .contact{display:flex;align-items:center;gap:3px}
  .contact svg{width:7px;height:7px}
</style>
</head>
<body>

<!-- Cover -->
<section class="slide slide--cover">
  <div class="brand brand--large cover__brand"><span class="brand__dot"></span>Vast KELP</div>
  <div class="cover__band">CLICK TO ADD TITLE</div>
  <p class="cover__subtitle">Lorem ipsum dolor sit amet, consectetur<br>adipisicing elit, sed do eiusmod tempor</p>
</section>

<!-- Contents -->
<section class="slide slide--contents">
  <svg class="header__mark" width="56" height="14" viewBox="0 0 56 14">
    <rect x="0" y="0" width="30" height="14" fill="var(--green)"/>
    <polygon points="30,0 37,0 33,14 26,14" fill="var(--green)"/>
    <polygon points="38,0 42,0 38,14 34,14" fill="var(--green)"/>
    <polygon points="43,0 47,0 43,14 39,14" fill="var(--green)"/>
    <polygon points="48,0 52,0 48,14 44,14" fill="var(--green)"/>
    <polygon points="53,0 56,0 53,14 49,14" fill="var(--green)"/>
  </svg>
  <h2 class="header__title">CLICK TO ADD TITLE</h2>
  <div class="brand brand--small header__brand"><span class="brand__dot"></span>Vast KELP</div>

  <ul class="toc">
    <li class="toc__row"><span class="toc__label">Lorem Ipsum is simply dummy text</span><span class="toc__leader"></span><span class="toc__page">1</span></li>
    <li class="toc__row toc__row--sub"><span class="toc__label">a) Of the printing and typesetting industry. Lorem Ipsum has been the try's</span><span class="toc__leader"></span><span class="toc__page">2</span></li>
    <li class="toc__row toc__row--sub"><span class="toc__label">b) Standard dummy text ever since the 1500s, when an unknown printer</span><span class="toc__leader"></span><span class="toc__page">2</span></li>
    <li class="toc__row"><span class="toc__label">Lorem Ipsum is simply dummy text is the basic dummy text</span><span class="toc__leader"></span><span class="toc__page">3</span></li>
    <li class="toc__row toc__row--sub"><span class="toc__label">make a type specimen book. It has survived not only five centuries</span><span class="toc__leader"></span><span class="toc__page">4</span></li>
    <li class="toc__row toc__row--sub"><span class="toc__label">leap into electronic typesetting, remaining</span><span class="toc__leader"></span><span class="toc__page">5</span></li>
    <li class="toc__row toc__row--sub"><span class="toc__label">larised in the 1960s with the release of Letraset sheets containing</span><span class="toc__leader"></span><span class="toc__page">6</span></li>
    <li class="toc__row"><span class="toc__label">Lorem Ipsum is simply dummy text</span><span class="toc__leader"></span><span class="toc__page">7</span></li>
    <li class="toc__row"><span class="toc__label">Lorem Ipsum is simply dummy textlorem ipsum is</span><span class="toc__leader"></span><span class="toc__page">7</span></li>
  </ul>

  <svg class="footer" viewBox="0 0 512 15" preserveAspectRatio="none">
    <polygon points="0,0 354,0 350,15 0,15" fill="var(--green)"/>
    <polygon points="360,0 512,0 512,15 356,15" fill="var(--green-dark)"/>
  </svg>
  <div class="footer__url" style="top:369px">www.vastkelp-labs.com</div>
</section>

<!-- Article -->
<section class="slide slide--article">
  <svg class="header__mark" width="56" height="14" viewBox="0 0 56 14">
    <rect x="0" y="0" width="30" height="14" fill="var(--green)"/>
    <polygon points="30,0 37,0 33,14 26,14" fill="var(--green)"/>
    <polygon points="38,0 42,0 38,14 34,14" fill="var(--green)"/>
    <polygon points="43,0 47,0 43,14 39,14" fill="var(--green)"/>
    <polygon points="48,0 52,0 48,14 44,14" fill="var(--green)"/>
    <polygon points="53,0 56,0 53,14 49,14" fill="var(--green)"/>
  </svg>
  <h2 class="header__title">CLICK TO ADD TITLE</h2>
  <div class="brand brand--small header__brand" style="left:412px">
    <span class="brand__dot"></span>Vast KELP</div>

  <h3 class="article__heading">Lorem ipsum dolor sit amet, consectetur adipisicing elit, sed</h3>
  <div class="article__columns">
    <p>Lorem Ipsum is simply dummy text of the printing and typesetting industry. Lorem Ipsum has been the industry's standard dummy text ever since the 1500s, when an unknown printer took a galley of type and scrambled it to make a type specimen book. It has survived not only five centuries, but also the leap into electronic typesetting, remaining essentially unchanged. It was popularised in the 1960s with the release of Letraset sheets containing Lorem Ipsum passages, and more recently with desktop publishing software including versions of Lorem Ipsum.</p>
    <p>It is a long established fact that a reader will be distracted by the readable content of a page when looking at its layout. The point of using Lorem Ipsum is that it has a more-or-less normal distribution of letters, as opposed to using 'Content here, content here', making it look like readable English. Many desktop publishing packages and web page editors now use Lorem Ipsum as their default model text, and a search for 'lorem ipsum' will uncover many web sites still in their infancy. Vari</p>
    <p>Contrary to popular belief, Lorem Ipsum is not simply random text. It has roots in a piece of classical Latin literature from 45 BC, making it over 2000 years old. A Latin professor at a college in Virginia, looked up one of the more obscure Latin words, consectetur, from a Lorem Ipsum passage, and going through the cites of the word in classical literature, discovered the undoubtable source. Lorem Ipsum comes from sections 1.10.32 and 1.10.33 of "de Finibus Bonorum et Malorum" (The Extremes of Good and Evil) by Cicero, written in 45 BC. This book is a treatise on the theory of ethics, very popular during the Renaissance. The first line of Lorem Ipsum, "Lorem ipsum dolor sit amet..", comes from a line in section 1.10.32.</p>
    <p>The standard chunk of Lorem Ipsum used since the 1500s is reproduced below for those interested. Sections 1.10.32 and 1.10.33 from "de Finibus Bonorum et Malorum" by Cicero are also reproduced in their exact original form, accompanied by English versions from the 1914 translation.</p>
    <p>There are many variations of passages of Lorem Ipsum available, but the majority have suffered alteration in some form, by injected humour, or randomised words which don't look even slightly believable. If you are going to use a passage of Lorem Ipsum, you need to be sure there isn't anything embarrassing hidden in the middle of text. All the Lorem Ipsum generators on</p>
  </div>

  <svg class="footer" viewBox="0 0 512 15" preserveAspectRatio="none">
    <polygon points="0,0 354,0 350,15 0,15" fill="var(--green)"/>
    <polygon points="360,0 512,0 512,15 356,15" fill="var(--green-dark)"/>
  </svg>
  <div class="footer__url" style="top:369px">www.vastkelp-labs.com</div>
</section>

<!-- Closing -->
<section class="slide slide--closing">
  <div class="brand brand--large closing__brand"><span class="brand__dot"></span>Vast KELP</div>
  <div class="closing__band">
    <span class="contact">
      <svg viewBox="0 0 10 10"><circle cx="5" cy="5" r="5" fill="#fff"/><path d="M3.2 2.6l1 1-.6.7c.4.8 1 1.4 1.8 1.8l.7-.6 1 1-.8.8C4.6 7.2 2.8 5.4 2.4 3.4z" fill="var(--green)"/></svg>
      +0 555.014.2790</span>
    <span class="contact">
      <svg viewBox="0 0 10 10"><circle cx="5" cy="5" r="5" fill="#fff"/><rect x="2.5" y="3.2" width="5" height="3.6" fill="var(--green)"/><path d="M2.5 3.2L5 5.2 7.5 3.2" stroke="#fff" stroke-width=".6" fill="none"/></svg>
      hello@vastkelp-labs.com</span>
    <span class="contact">
      <svg viewBox="0 0 10 10"><circle cx="5" cy="5" r="5" fill="#fff"/><circle cx="5" cy="5" r="2.6" fill="none" stroke="var(--green)" stroke-width=".7"/><path d="M2.4 5h5.2M5 2.4c-1.2 1.6-1.2 3.6 0 5.2M5 2.4c1.2 1.6 1.2 3.6 0 5.2" stroke="var(--green)" stroke-width=".5" fill="none"/></svg>
      www.vastkelp-labs.net</span>
  </div>
</section>

</body>
</html>
```